Brisko Sky Park needs a new upscale business card design for our high end aircraft hangar complex

Brisko Sky Park (BSP) is a large, upscale jet hangar complex in the US housing expensive aircraft. We need a new business card design, using our current logo. We will be attending a industry convention and need a card design that will stand out and be remembered by aircraft owners and private pilots.

Target Market(s)

Aircraft pilots or owners looking for a new upscale hangar

Industry/Entity Type

Airport

Contact Information for Business Card

I like to use very heavy card stock, 400#, double sided. Square, no rounded edges please.

Colors
3276b5
0255a3
85abd2

Requirements
Must have
• An expensive, classy design, vivid colors.
Nice to have
• Needs to look very expensive and classy, and have some "pop". Designer must be able to download or copy my current typeface or fonts.
• One card side might be black with the "Logo and Brisko Sky Park Double line image in blue (or try gold, or glossy black), and perhaps have a grayed out "K480 jet silhouette". The other card side would have our contact info, and perhaps the "BSP Logo only". I'd like my contact info 'stacked', not in a paragraph format.
Should not have
• Should not look "too busy". Having a double-sided card will help.

```html
<!DOCTYPE html>
<html lang="en">
<head>
<meta charset="utf-8">
<title>Brisko Sky Park – Business Card</title>
<link rel="stylesheet" href="https://fonts.googleapis.com/css2?family=PT+Sans:wght@400;700&display=swap">
<style>
  :root {
    --card-black: #030506;
    --card-edge: #1a1c1e;
    --gold: #f7d400;
    --blue: #0a55a3;
    --blue-light: #3276b5;
    --page: #ffffff;
    --jet-dark: #1c1e20;
    --jet-light: #6d7074;
  }
  * { margin: 0; padding: 0; box-sizing: border-box; }
  html, body {
    width: 1025px; height: 1200px; overflow: hidden;
    background: var(--page);
    font-family: "PT Sans", "Myriad Pro", Arial, sans-serif;
  }
  .canvas { position: relative; width: 1025px; height: 1200px; }

  .card {
    position: absolute; left: 0; width: 1025px; height: 587px;
    background: var(--card-black);
    border: 2px solid var(--card-edge);
  }
  .card--front { top: 0; }
  .card--back { top: 613px; }

  .card__frame {
    position: absolute; left: 38px; top: 34px; width: 950px; height: 517px;
    border: 2px solid var(--gold);
  }

  /* front */
  .jet-art {
    position: absolute; left: 126px; top: 180px; width: 255px; height: 150px;
    background: radial-gradient(ellipse at 50% 55%, var(--jet-light) 0%, var(--jet-dark) 55%, transparent 72%);
    opacity: .75;
  }
  .brand-mark {
    position: absolute; left: 0; width: 100%; text-align: center;
    color: var(--gold); font-weight: 700; line-height: 1;
  }
  .brand-mark--initials { top: 150px; font-size: 150px; letter-spacing: 6px; }
  .brand-mark--name { top: 330px; font-size: 104px; }

  /* back */
  .back-logo {
    position: absolute; left: 112px; top: 188px; width: 320px; text-align: center;
    color: var(--gold); font-weight: 700; font-size: 110px; line-height: 1; letter-spacing: 4px;
  }
  .jet-art--small {
    position: absolute; left: 165px; top: 322px; width: 215px; height: 30px;
    background: radial-gradient(ellipse at 50% 50%, var(--jet-light) 0%, var(--jet-dark) 50%, transparent 75%);
    opacity: .7;
  }

  .contact-name {
    position: absolute; right: 66px; top: 102px;
    color: var(--gold); font-size: 47px; font-weight: 400; line-height: 1;
  }
  .contact-list { list-style: none; }
  .contact-item {
    position: absolute; right: 64px; height: 44px;
    display: flex; align-items: center; gap: 22px;
    color: var(--gold); font-size: 27px; line-height: 1;
  }
  .contact-item:nth-child(1) { top: 184px; }
  .contact-item:nth-child(2) { top: 264px; }
  .contact-item:nth-child(3) { top: 343px; }
  .contact-item:nth-child(4) { top: 422px; }
  .contact-icon { width: 44px; height: 44px; flex: none; }
</style>
</head>
<body>
<main class="canvas">

  <section class="card card--front" aria-label="Card front">
    <div class="card__frame"></div>
    <div class="jet-art" role="img" aria-label="Grey business jet in banking flight"></div>
    <div class="brand-mark brand-mark--initials">BSP</div>
    <div class="brand-mark brand-mark--name">Brisko Sky Park</div>
  </section>

  <section class="card card--back" aria-label="Card back">
    <div class="card__frame"></div>
    <div class="back-logo">BSP</div>
    <div class="jet-art--small" role="img" aria-label="Grey business jet seen head-on"></div>

    <div class="contact-name">Your Name</div>
    <ul class="contact-list">
      <li class="contact-item">
        <span>+1 123-456-7890</span>
        <svg class="contact-icon" viewBox="0 0 44 44" aria-hidden="true">
          <circle cx="22" cy="22" r="20.5" fill="var(--blue)" stroke="var(--gold)" stroke-width="2"/>
          <path d="M15 12c1.5-1 3-.5 3.8 1l2 3.6c.6 1.2 0 2.2-1 2.9l-1.2.8c1 2.6 3 4.8 5.6 6l.9-1.1c.8-1 1.9-1.4 3-.7l3.5 2.1c1.4.8 1.6 2.3.6 3.6l-1.4 1.6c-1.3 1.4-3.6 1.7-6 .5-5.4-2.6-9.5-7-11.4-12.6-.8-2.3-.3-4.5 1.2-5.9z" fill="none" stroke="var(--gold)" stroke-width="2"/>
        </svg>
      </li>
      <li class="contact-item">
        <span>www.yoursite.com</span>
        <svg class="contact-icon" viewBox="0 0 44 44" aria-hidden="true">
          <circle cx="22" cy="22" r="20.5" fill="var(--blue)" stroke="var(--gold)" stroke-width="2"/>
          <circle cx="22" cy="22" r="13" fill="none" stroke="var(--gold)" stroke-width="2"/>
          <ellipse cx="22" cy="22" rx="5.5" ry="13" fill="none" stroke="var(--gold)" stroke-width="2"/>
          <path d="M9 22h26M11 15h22M11 29h22" stroke="var(--gold)" stroke-width="2"/>
        </svg>
      </li>
      <li class="contact-item">
        <span>contact@yoursite.com</span>
        <svg class="contact-icon" viewBox="0 0 44 44" aria-hidden="true">
          <circle cx="22" cy="22" r="20.5" fill="var(--blue)" stroke="var(--gold)" stroke-width="2"/>
          <rect x="12" y="15" width="20" height="14" fill="var(--gold)"/>
          <path d="M12 15l10 8 10-8M12 29l7-6M32 29l-7-6" fill="none" stroke="var(--blue)" stroke-width="1.8"/>
        </svg>
      </li>
      <li class="contact-item">
        <span>Street Address, city, USA</span>
        <svg class="contact-icon" viewBox="0 0 44 44" aria-hidden="true">
          <circle cx="22" cy="22" r="20.5" fill="var(--blue)" stroke="var(--gold)" stroke-width="2"/>
          <path d="M22 33c-4.5-5.5-8-9.5-8-14a8 8 0 0 1 16 0c0 4.5-3.5 8.5-8 14z" fill="none" stroke="var(--gold)" stroke-width="2"/>
          <circle cx="22" cy="19" r="3" fill="none" stroke="var(--gold)" stroke-width="2"/>
        </svg>
      </li>
    </ul>
  </section>

</main>
</body>
</html>
```